Corvanta Business cards template

We're looking for something modern and elegant. We are a reseller of technology (computers, datacenter, etc). Color theme would be "only" white with the incorporation of the blue that's present on our website (Corvanta.com) and logo file. We would like for the card to provide all the necessary info for the specific person (Phone#, fax#, email, name, website URL) . I'm attaching the logo file to this request. Please have it show Calgary/San Diego somewhere, without providing specific addresses.

Target Market(s)

All b2b

Industry/Entity Type

Business

Contact Information for Business Card

Please have the color scheme be represented by only the white and blue from our website (Corvanta.com) and logo. We would like to logo on the card, but not big and overwhelming. This card will be used as a template for anybody within the company, it should display the user's name, phone#, fax#, email, job title and website URL. Please have it show Calgary/San Diego somewhere, without providing our specific addresses. Really, we're looking for a clean, simple and elegant look.

Font styles to use
Serif

Requirements
Must have
• Please see card details
Nice to have
• Please see card details
Should not have
• Anything tacky or tagline.

```html
<!DOCTYPE html>
<html lang="en">
<head>
<meta charset="utf-8">
<title>Corvanta Business Cards</title>
<link href="https://fonts.googleapis.com/css2?family=Roboto:wght@400;500&family=Roboto+Condensed:wght@500;700&display=swap" rel="stylesheet">
<style>
  :root {
    --backdrop: #262626;
    --card-white: #f3f3f3;
    --brand-blue: #0b6bb8;
    --brand-blue-light: #1a8bd6;
    --text-grey: #4f4f4f;
    --white: #ffffff;
  }
  * { margin: 0; padding: 0; box-sizing: border-box; }
  html, body { width: 1200px; height: 960px; overflow: hidden; }
  body {
    background: var(--backdrop);
    position: relative;
    font-family: "Roboto", Arial, sans-serif;
  }
  .card {
    position: absolute;
    width: 600px;
    height: 342px;
    border-radius: 20px;
    overflow: hidden;
  }
  .card-front { left: 314px; top: 114px; background: var(--card-white); }
  .card-back { left: 311px; top: 472px; background: var(--brand-blue); }

  .brand-name {
    position: absolute;
    left: 0; right: 0;
    text-align: center;
    font-family: "Roboto", Arial, sans-serif;
    font-weight: 500;
    font-size: 50px;
    letter-spacing: 1px;
  }
  .card-front .brand-name { top: 68px; color: var(--brand-blue); }
  .card-back .brand-name { top: 120px; color: var(--white); }

  .holder-name {
    position: absolute; left: 0; right: 0; top: 172px;
    text-align: center;
    font-family: "Roboto Condensed", Arial, sans-serif;
    font-weight: 700; font-size: 23px;
    color: var(--brand-blue);
  }
  .holder-title {
    position: absolute; left: 0; right: 0; top: 201px;
    text-align: center;
    font-family: "Roboto Condensed", Arial, sans-serif;
    font-weight: 500; font-size: 15px;
    color: var(--brand-blue-light);
  }
  .office-cities {
    position: absolute; left: 0; right: 0; top: 240px;
    text-align: center;
    font-size: 14.5px; color: var(--text-grey);
  }
  .contact-row {
    position: absolute; left: 0; right: 0; top: 262px;
    display: flex; justify-content: center; align-items: center; gap: 6px;
    font-size: 14.5px; color: var(--text-grey);
  }
  .contact-item { display: flex; align-items: center; gap: 2px; }
  .contact-icon { width: 13px; height: 13px; fill: var(--brand-blue); }

  .front-swoosh { position: absolute; left: 0; bottom: 0; width: 600px; height: 60px; }
  .front-url {
    position: absolute; left: 0; right: 0; top: 316px;
    text-align: center;
    font-size: 13px; letter-spacing: 3px;
    color: var(--white);
  }

  .back-pattern-area { position: absolute; inset: 0; background: var(--brand-blue); }
  .back-url-strip {
    position: absolute; left: 0; right: 0; top: 284px; height: 30px;
    background: var(--white);
    display: flex; align-items: center; justify-content: center;
    font-size: 13px; font-weight: 500; letter-spacing: 4px;
    color: var(--brand-blue);
  }
</style>
</head>
<body>
  <section class="card card-front">
    <div class="brand-name">Corvanta</div>
    <div class="holder-name">DANIEL HARTLEY</div>
    <div class="holder-title">CEO/FOUNDER</div>
    <div class="office-cities">Calgary/San Diego</div>
    <div class="contact-row">
      <span class="contact-item">
        <svg class="contact-icon" viewBox="0 0 24 24" aria-hidden="true"><path d="M6.6 10.8a15.1 15.1 0 0 0 6.6 6.6l2.2-2.2c.3-.3.7-.4 1-.2 1.1.4 2.3.6 3.6.6.6 0 1 .4 1 1V20c0 .6-.4 1-1 1A17 17 0 0 1 3 4c0-.6.4-1 1-1h3.5c.6 0 1 .4 1 1 0 1.3.2 2.5.6 3.6.1.3 0 .7-.2 1z"/></svg>
        1-855-604-CORV (2678)
      </span>
      <span class="contact-item">
        <svg class="contact-icon" viewBox="0 0 24 24" aria-hidden="true"><path d="M6 3h12v5H6zM3 9h18v9h-3v3H6v-3H3zm5 6v4h8v-4z"/></svg>
        482 555 0174
      </span>
      <span class="contact-item">
        <svg class="contact-icon" viewBox="0 0 24 24" aria-hidden="true"><path d="M2 5h20v14H2zm2 2v1l8 5 8-5V7l-8 5z"/></svg>
        info@corvanta.com
      </span>
    </div>
    <svg class="front-swoosh" viewBox="0 0 600 60" aria-hidden="true">
      <path d="M0 60 L0 54 Q300 -14 600 54 L600 60 Z" fill="var(--brand-blue)"/>
      <path d="M8 44 Q300 -16 592 44" fill="none" stroke="var(--brand-blue-light)" stroke-width="2"/>
    </svg>
    <div class="front-url">www.corvanta.com</div>
  </section>

  <section class="card card-back">
    <div class="back-pattern-area" role="img" aria-label="Repeating blue ring pattern background"></div>
    <div class="brand-name">Corvanta</div>
    <div class="back-url-strip">www.corvanta.com</div>
  </section>
</body>
</html>
```